Keystone Haulers Billboard design

I need two billboard designs using our logo and adding a few words Looking for a black background with our logo and wording in either purple or white.

need it to have our website keystonehaulers-example.com. phone number 555 201 4387

Also have 16/20/30 yard dumpsters available!

one billboard is size 7x21 feet the other is 15x 21 ft

Target Market(s)

Contractors, home owners

Requirements
Must have
• Use font similar to logo that is eye catching

```html
<!DOCTYPE html>
<html lang="en">
<head>
<meta charset="utf-8">
<title>Keystone Haulers Billboards</title>
<link rel="stylesheet" href="https://fonts.googleapis.com/css2?family=Bebas+Neue&family=Montserrat:wght@500;600;800&display=swap">
<style>
  :root {
    --canvas: #d1d2d4;
    --board-black: #0b0a0d;
    --swirl-purple: #7a2a86;
    --brand-purple: #7f3f98;
    --white: #ffffff;
  }
  * { box-sizing: border-box; margin: 0; padding: 0; }
  html, body { width: 1153px; height: 1200px; overflow: hidden; }
  body {
    background: var(--canvas);
    position: relative;
    font-family: "Montserrat", Arial, sans-serif;
  }
  .billboard {
    position: absolute;
    left: 239px;
    width: 676px;
    background: var(--board-black);
    overflow: hidden;
  }
  .billboard--wide { top: 237px; height: 225px; }
  .billboard--tall { top: 494px; height: 482px; }

  .billboard__texture {
    position: absolute; inset: 0;
    background:
      radial-gradient(ellipse at 15% 20%, rgba(122,42,134,0.30), transparent 45%),
      radial-gradient(ellipse at 85% 70%, rgba(122,42,134,0.35), transparent 50%),
      radial-gradient(ellipse at 40% 100%, rgba(122,42,134,0.40), transparent 45%),
      var(--board-black);
  }

  .brand-name {
    position: absolute; left: 0; right: 0;
    text-align: center;
    color: var(--white);
    font-weight: 800;
    letter-spacing: 0.5px;
    white-space: nowrap;
  }
  .billboard--wide .brand-name { top: 30px; font-size: 36px; line-height: 44px; }
  .billboard--tall .brand-name { top: 46px; font-size: 62px; line-height: 76px; }

  .headline {
    position: absolute; left: 0; right: 0;
    text-align: center;
    color: var(--white);
    font-family: "Bebas Neue", "Oswald", sans-serif;
    font-weight: 400;
    white-space: nowrap;
    transform-origin: center top;
  }
  .billboard--wide .headline {
    top: 96px; font-size: 46px; line-height: 46px;
    transform: scaleX(0.86);
  }
  .billboard--tall .headline {
    top: 160px; font-size: 76px; line-height: 66px;
    transform: scaleX(0.88);
  }

  .sizes {
    position: absolute;
    background: var(--brand-purple);
    color: var(--white);
    font-weight: 500;
    text-align: center;
    white-space: nowrap;
  }
  .sizes__numbers {
    display: inline-block;
    background: var(--white);
    color: var(--brand-purple);
    font-weight: 600;
  }
  .billboard--wide .sizes {
    left: 127px; top: 148px; width: 421px; height: 31px;
    font-size: 20px; line-height: 31px;
  }
  .billboard--wide .sizes__numbers { padding: 0 2px; line-height: 25px; }
  .billboard--tall .sizes {
    left: 122px; top: 322px; width: 432px; height: 105px;
    font-size: 38px; line-height: 46px; padding-top: 6px;
  }
  .billboard--tall .sizes__numbers { padding: 0 6px; line-height: 42px; }

  .contact-bar {
    position: absolute; left: 0; right: 0; bottom: 0; height: 32px;
    background: var(--white);
    display: flex; justify-content: space-between; align-items: center;
    padding: 0 26px;
    color: var(--brand-purple);
    font-weight: 500;
    font-size: 20px;
  }
  .contact-bar__item { display: flex; align-items: center; gap: 8px; }
  .contact-bar__icon { width: 20px; height: 20px; flex: none; }
</style>
</head>
<body>

  <section class="billboard billboard--wide">
    <div class="billboard__texture" role="img" aria-label="Dark marbled background with purple swirling lines"></div>
    <div class="brand-name">Keystone Haulers</div>
    <h1 class="headline">Residential &amp; Commercial Dumpster Rentals</h1>
    <p class="sizes">We have <span class="sizes__numbers">16 / 20 / 30</span> yard dumpsters</p>
    <footer class="contact-bar">
      <span class="contact-bar__item">
        <svg class="contact-bar__icon" viewBox="0 0 20 20"><rect width="20" height="20" rx="2" fill="#7f3f98"/><path d="M6 4.5l2.2 2.6-1.3 1.5c.8 1.7 2 2.9 3.6 3.7l1.5-1.3 2.6 2.2-1.4 2c-4.4-.4-8.4-4.4-8.8-8.8z" fill="#fff"/></svg>
        555 201 4387
      </span>
      <span class="contact-bar__item">
        <svg class="contact-bar__icon" viewBox="0 0 20 20"><rect width="20" height="20" rx="2" fill="#7f3f98"/><circle cx="10" cy="10" r="6" fill="none" stroke="#fff" stroke-width="1.3"/><ellipse cx="10" cy="10" rx="2.6" ry="6" fill="none" stroke="#fff" stroke-width="1.2"/><path d="M4 10h12M5 7h10M5 13h10" stroke="#fff" stroke-width="1.1"/></svg>
        keystonehaulers-example.com
      </span>
    </footer>
  </section>

  <section class="billboard billboard--tall">
    <div class="billboard__texture" role="img" aria-label="Dark marbled background with purple swirling lines"></div>
    <div class="brand-name">Keystone Haulers</div>
    <h1 class="headline">Residential &amp; Commercial<br>Dumpster Rentals</h1>
    <p class="sizes">We have <span class="sizes__numbers">16 / 20 / 30</span><br>yard dumpsters</p>
    <footer class="contact-bar">
      <span class="contact-bar__item">
        <svg class="contact-bar__icon" viewBox="0 0 20 20"><rect width="20" height="20" rx="2" fill="#7f3f98"/><path d="M6 4.5l2.2 2.6-1.3 1.5c.8 1.7 2 2.9 3.6 3.7l1.5-1.3 2.6 2.2-1.4 2c-4.4-.4-8.4-4.4-8.8-8.8z" fill="#fff"/></svg>
        555 201 4387
      </span>
      <span class="contact-bar__item">
        <svg class="contact-bar__icon" viewBox="0 0 20 20"><rect width="20" height="20" rx="2" fill="#7f3f98"/><circle cx="10" cy="10" r="6" fill="none" stroke="#fff" stroke-width="1.3"/><ellipse cx="10" cy="10" rx="2.6" ry="6" fill="none" stroke="#fff" stroke-width="1.2"/><path d="M4 10h12M5 7h10M5 13h10" stroke="#fff" stroke-width="1.1"/></svg>
        keystonehaulers-example.com
      </span>
    </footer>
  </section>

</body>
</html>
```